Clean Energy Brand - Business Card and Letterhead Designs

Hi, everyone! We need a graphic designer who has experience working with the energy sector. We want help designing a perfect two-sided business card and letterhead for a clean energy company we've been assisting. We have a great new logo and all of the associated files.Our client is looking for a design that is "disruptive," "future-facing," "masculine," "bold," and "empowering." The colours of the logo are navy blue and orange and are meant to stand out. We'll need all ownership and copyright paperwork as well as first proofs in a 48-hour period.

Target Market(s)

Government; Non-Profits; Clean Energy Industry; Municipalities; North American Energy Sector

Industry/Entity Type

Power Generation

Requirements
Must have
• A matching business card and letterhead design
Should not have
• Must not be from a template

```html
<!DOCTYPE html>
<html lang="en">
<head>
<meta charset="utf-8">
<title>Solvanta Clean Energy — Stationery</title>
<link href="https://fonts.googleapis.com/css2?family=Lato:wght@300;400;700&family=Roboto:wght@400;500&family=Great+Vibes&display=swap" rel="stylesheet">
<style>
  :root{
    --navy:#1d1f5e;
    --orange:#e8562a;
    --ink:#3a3a3a;
    --muted:#666a70;
    --paper:#ffffff;
    --stage:#e4e4e5;
  }
  *{box-sizing:border-box;margin:0;padding:0}
  html,body{width:1200px;height:955px;overflow:hidden;background:var(--stage)}
  body{position:relative;font-family:'Lato',sans-serif;color:var(--ink)}

  /* Letterhead */
  .letterhead{position:absolute;left:70px;top:45px;width:610px;height:862px;background:var(--paper);
    box-shadow:0 2px 10px rgba(0,0,0,.12)}
  .brand{text-align:center}
  .brand-name{font-family:'Lato',sans-serif;font-weight:700;color:var(--navy);letter-spacing:.5px;line-height:1}
  .brand-tag{font-family:'Lato',sans-serif;font-weight:400;color:var(--orange);letter-spacing:4px;line-height:1}
  .letterhead .brand{position:absolute;top:70px;left:0;right:0}
  .letterhead .brand-name{font-size:34px}
  .letterhead .brand-tag{font-size:11px;margin-top:4px}

  .letter{position:absolute;left:82px;right:82px;top:196px;font-size:10px;line-height:1.5;font-weight:400}
  .letter-date{margin-bottom:22px}
  .recipient{margin-bottom:30px}
  .recipient strong{font-weight:700;color:#111}
  .salutation{margin-bottom:14px}
  .letter p.body{text-align:justify;margin-bottom:16px}
  .closing{margin-top:46px}
  .signature{font-family:'Great Vibes',cursive;font-size:22px;color:#222;margin-top:2px;margin-left:6px}

  .letter-footer{position:absolute;left:52px;bottom:24px;display:flex;font-family:'Roboto',sans-serif;
    font-size:10.5px;color:var(--muted);line-height:1.45}
  .footer-col{padding-right:12px}
  .footer-col + .footer-col{border-left:1px solid #9a9a9a;padding-left:12px}
  .contact-line{display:flex;align-items:center;gap:6px}
  .contact-line svg{width:8px;height:8px;flex:none}

  /* Business cards */
  .card{position:absolute;left:690px;width:480px;height:266px;box-shadow:0 3px 8px rgba(0,0,0,.18)}
  .card-back{top:150px;background:var(--navy)}
  .card-back .brand{position:absolute;left:0;right:0;top:92px}
  .card-back .brand-name{color:#fff;font-size:36px}
  .card-back .brand-tag{color:#fff;font-size:12px;margin-top:6px}

  .card-front{top:340px;top:338px;background:var(--paper);top:338px}
  .card-front{top:338px}
  .card-front .brand{position:absolute;left:38px;top:62px;text-align:center}
  .card-front .brand-name{font-size:24px}
  .card-front .brand-tag{font-size:7.5px;letter-spacing:2.5px;margin-top:3px}
  .holder{position:absolute;right:40px;top:36px;text-align:right}
  .holder-name{font-family:'Lato',sans-serif;font-weight:700;color:var(--navy);font-size:12.5px}
  .holder-role{font-family:'Lato',sans-serif;color:var(--orange);font-size:9px}
  .card-details{position:absolute;left:42px;top:138px;font-family:'Roboto',sans-serif;font-size:9px;
    color:var(--muted);line-height:1.35}
  .card-details .address{margin-bottom:10px}
  .card-details .contact-line svg{width:7px;height:7px}
</style>
</head>
<body>

<svg width="0" height="0" style="position:absolute" aria-hidden="true">
  <defs>
    <symbol id="i-phone" viewBox="0 0 10 10"><path d="M2 1l2 0 1 2.5-1.2 1a5 5 0 0 0 2.7 2.7l1-1.2L10 7v2c0 .6-.5 1-1 1A9 9 0 0 1 0 1c0-.5.4-1 1-1z" fill="#e8562a"/></symbol>
    <symbol id="i-mobile" viewBox="0 0 10 10"><rect x="2.5" y=".5" width="5" height="9" rx="1" fill="none" stroke="#e8562a" stroke-width="1.2"/><circle cx="5" cy="8" r=".6" fill="#e8562a"/></symbol>
    <symbol id="i-mail" viewBox="0 0 10 10"><rect x=".6" y="2" width="8.8" height="6" fill="none" stroke="#e8562a" stroke-width="1.1"/><path d="M.8 2.3L5 5.6l4.2-3.3" fill="none" stroke="#e8562a" stroke-width="1.1"/></symbol>
    <symbol id="i-globe" viewBox="0 0 10 10"><circle cx="5" cy="5" r="4.5" fill="#e8562a"/><path d="M.8 5h8.4M5 .6c-2.4 2.6-2.4 6.2 0 8.8M5 .6c2.4 2.6 2.4 6.2 0 8.8" fill="none" stroke="#fff" stroke-width=".7"/></symbol>
  </defs>
</svg>

<section class="letterhead">
  <header class="brand">
    <div class="brand-name">Solvanta</div>
    <div class="brand-tag">CLEAN ENERGY</div>
  </header>

  <article class="letter">
    <div class="letter-date">01 January 2050</div>
    <div class="recipient">
      <strong>Company (Pvt) Ltd.</strong><br>
      PO Box 4120 Ridgeline Rd<br>
      Northfield Country 4120
    </div>
    <div class="salutation">Dear Andrew Colby,</div>
    <p class="body">Lorem ipsum dolor sit amet, consectetuer adipiscing elit, sed diam nonummy nibh euismod tincidunt ut laoreet dolore magna aliquam erat volutpat. Ut wisi enim ad minim veniam, quis nostrud exerci tation ullamcorper suscipit lobortis nisl ut aliquip ex ea commodo consequat. Duis dolore te feugait nulla facilisi. Nam liber tempor cum soluta nobis eleifend option congue nihil imperdiet doming id quod mazim placerat facer possim assum. Lorem ipsum dolor sit amet, consectetuer adipiscing elit, sed diam nonummy nibh euismod tincidunt ut laoreet dolore magna aliquam erat volutpat. Ut wisi enim ad minim veniam, quis nostrud exerci tation ullamcorper suscipit lobortis nisl ut aliquip ex ea commodo consequat.</p>
    <p class="body">Consectetuer adipiscing elit, sed diam nonummy nibh euismod tincidunt ut laoreet dolore magna aliquam erat volutpat. Ut wisi enim ad minim veniam, quis nostrud exerci tation ullamcorper suscipit lobortis nisl ut aliquip ex ea commodo consequat. Consectetuer adipiscing elit, sed diam nonummy nibh euismod tincidunt ut laoreet dolore magna aliquam erat volutpat. Ut wisi enim ad minim veniam, quis nostrud exerci tation ullamcorper suscipit lobortis nisl ut aliquip ex ea commodo consequat.</p>
    <p class="body">Consectetuer adipiscing elit, sed diam nonummy nibh euismod tincidunt ut laoreet dolore magna aliquam erat volutpat. Ut wisi enim ad minim veniam, quis nostrud exerci tation ullamcorper suscipit lobortis nisl ut aliquip ex ea commodo consequat. Consectetuer adipiscing elit, sed diam nonummy nibh euismod tincidunt ut laoreet dolore magna aliquam erat volutpat. Ut wisi enim ad minim veniam, quis nostrud exerci tation ullamcorper suscipit lobortis nisl ut aliquip ex ea commodo consequat.</p>
    <div class="closing">Sincerely Yours</div>
    <div class="signature">Daniel Whitmore</div>
  </article>

  <footer class="letter-footer">
    <div class="footer-col">
      <div class="contact-line"><svg><use href="#i-phone"/></svg>210.555.0142</div>
      <div class="contact-line"><svg><use href="#i-mobile"/></svg>310.555.0187</div>
      <div class="contact-line"><svg><use href="#i-mail"/></svg>hello@solvantaenergy.com</div>
    </div>
    <div class="footer-col">
      <div>PO Box 4120 Ridgeline Rd</div>
      <div>Northfield Country 4120</div>
      <div class="contact-line"><svg><use href="#i-globe"/></svg>www.solvantaenergy.com</div>
    </div>
  </footer>
</section>

<section class="card card-back">
  <div class="brand">
    <div class="brand-name">Solvanta</div>
    <div class="brand-tag">CLEAN ENERGY</div>
  </div>
</section>

<section class="card card-front">
  <div class="brand">
    <div class="brand-name">Solvanta</div>
    <div class="brand-tag">CLEAN ENERGY</div>
  </div>
  <div class="holder">
    <div class="holder-name">Marcus Ellery</div>
    <div class="holder-role">Managing Director</div>
  </div>
  <div class="card-details">
    <div class="address">PO Box 4120 Ridgeline Rd<br>Northfield Country 4120</div>
    <div class="contact-line"><svg><use href="#i-phone"/></svg>210.555.0142</div>
    <div class="contact-line"><svg><use href="#i-mobile"/></svg>310.555.0187</div>
    <div class="contact-line"><svg><use href="#i-mail"/></svg>hello@solvantaenergy.com</div>
    <div class="contact-line"><svg><use href="#i-globe"/></svg>www.solvantaenergy.com</div>
  </div>
</section>

</body>
</html>
```